Winery needs MailChimp newsletter

Hi
We have a small vineyard in Australia and need a newsletter designed to send out whenever we release a new vintage or there's some special news - approx 4 times per year.
We would like the design [added: including colours etc] to be consistent with our website:
www.bertolvi.com.au
(let us know if you need info re colours, fonts etc)
Also see the label designs on our website under Wines / Pinot Gris and Wines / Pinot Noir, to get more of a look and feel for our brand.
We plan on using mailchimp to send the newsletter out (but let us know if you'd recommend a different approach). [added: we think we'll need the mailchimp coding/html]
We're uploading the logo, a photo of a misty morning that's been used on our marketing materials in the past, as well as a photo of the current vintage that this next newsletter will announce the release of [added: it's a photo of a wine barrel, please show the whole barrel, not just the top of the barrel]. If you see other images on the website you would like to incorporate etc, please let us know.
[added: we've also uploaded an image of the grey iron shed from the logo, to be used eg as a header/footer]
Please allow space for a short intro paragraph (approx. 25-50 words), and a second area for more detailed information (approx. 50-75 words), [added: and a third area for wrapping up/other info (approx. 25-50 words)]
Lastly, we need the newsletter to link to/incorporate a pdf order form which will also be uploaded.
Thank you for your interest in this project - please don't hesitate to let us know what questions you have, thanks!
Maren T.

```html
<!DOCTYPE html>
<html lang="en">
<head>
<meta charset="utf-8">
<title>Bertolvi Single Vineyard – Newsletter</title>
<link rel="stylesheet" href="https://fonts.googleapis.com/css2?family=Cinzel:wght@400&family=Libre+Baskerville:ital,wght@1,700&family=Arimo:wght@400&display=swap">
<style>
  :root {
    --mauve: #d7c5c6;
    --mauve-text: #6f6264;
    --mint: #dfe8e5;
    --paper: #ffffff;
    --cream: #f2f0ea;
    --brown: #5f5347;
    --nav: #8a7c70;
    --rule: #cfcac4;
    --body: #6a6a6a;
    --teal: #a6d4d3;
    --ink: #1e1e1e;
    --stripe-dark: #8c8884;
    --stripe-light: #d8d4cf;
  }
  * { box-sizing: border-box; margin: 0; padding: 0; }
  html, body { width: 1200px; height: 3172px; overflow: hidden; }
  body { position: relative; background: var(--mint); font-family: "Arimo", Arial, sans-serif; color: var(--body); }

  .notice { position: absolute; left: 0; top: 0; width: 1200px; height: 80px; background: var(--mauve);
    display: flex; align-items: center; justify-content: center; font-size: 22px; color: var(--mauve-text); }
  .notice a { color: var(--mauve-text); }

  .sheet { position: absolute; left: 24px; top: 100px; width: 1152px; height: 2874px; background: var(--paper); }

  .masthead { position: absolute; left: 0; top: 0; width: 1152px; height: 265px; background: var(--cream); text-align: center; }
  .brand { padding-top: 20px; font-family: "Cinzel", serif; font-size: 76px; letter-spacing: 4px; color: var(--brown); line-height: 1.1; }
  .brand-sub { font-family: "Cinzel", serif; font-size: 28px; color: var(--brown); letter-spacing: 1px; margin-top: -4px; }
  .masthead hr { position: absolute; left: 78px; top: 154px; width: 996px; border: 0; border-top: 2px solid var(--rule); }
  .nav { position: absolute; left: 0; top: 194px; width: 1152px; display: flex; justify-content: center; gap: 22px;
    font-size: 25px; letter-spacing: 4px; color: var(--nav); }
  .nav .dot { letter-spacing: 0; }

  .hero { position: absolute; left: 0; top: 265px; width: 1152px; height: 1155px;
    background: linear-gradient(180deg, #c9ccc8 0%, #b8bdb4 35%, #8f9c84 60%, #5f7f3f 80%, #6e8f49 100%); }

  .headline { position: absolute; left: 0; top: 1455px; width: 1152px; text-align: center; line-height: 88px;
    font-family: "Libre Baskerville", serif; font-style: italic; font-weight: 700; font-size: 66px; color: var(--brown); }
  .rule { position: absolute; left: 84px; width: 984px; border-top: 2px solid var(--rule); }
  .rule.upper { top: 1584px; }
  .rule.lower { top: 1732px; }
  .rule.closing { top: 2675px; }
  .facts { position: absolute; left: 0; top: 1612px; width: 1152px; text-align: center; font-size: 23px; line-height: 29px; color: var(--body); }

  .feature { position: absolute; top: 1763px; width: 546px; height: 530px; }
  .feature.vineyard { left: 16px; }
  .feature.winemaking { left: 586px; }
  .feature .photo { width: 546px; height: 300px; }
  .vineyard .photo { background: radial-gradient(circle at 45% 50%, #5b6283 0%, #3f4566 45%, #a7b99a 80%, #dfe3d8 100%); }
  .winemaking .photo { background: linear-gradient(135deg, #6b4a2f 0%, #a77a4e 45%, #8c6440 75%, #3c2a1c 100%); }
  .feature h2 { font-weight: 400; font-size: 46px; color: var(--teal); margin-top: 18px; line-height: 1; }
  .feature p { font-size: 21.5px; line-height: 28px; color: var(--body); margin-top: 10px; }
  .feature .more { position: absolute; right: 6px; top: 496px; font-size: 22px; letter-spacing: 1px; color: var(--body); text-decoration: none; }

  .release { position: absolute; left: 0; top: 2305px; width: 1152px; height: 312px; overflow: hidden;
    background: linear-gradient(90deg, #d6d4d1 0%, #eeedeb 30%, #e9e7e3 50%, #8a8682 75%, #6f6b67 100%); }
  .release .wine { position: absolute; left: 520px; top: 0; width: 632px; height: 312px;
    background: radial-gradient(ellipse at 30% 75%, #5a1520 0%, #7a2a33 18%, rgba(120,118,114,0) 40%); }
  .release-copy { position: absolute; left: 64px; top: 40px; width: 480px; text-align: center; color: var(--ink); }
  .release-copy .title { font-size: 70px; line-height: 66px; letter-spacing: -2px; white-space: nowrap; }
  .release-copy .source { font-size: 16px; line-height: 18px; margin-top: 12px; }
  .release-copy .order { display: inline-flex; align-items: center; gap: 10px; font-size: 30px; line-height: 36px; margin-top: 10px; }

  .tasting { position: absolute; left: 60px; top: 2700px; width: 1032px; text-align: center; font-size: 22px; line-height: 28px; color: var(--body); }
  .served { margin-top: 14px; }

  .footer { position: absolute; left: 0; top: 2994px; width: 1200px; height: 92px; background: var(--mauve);
    font-size: 20px; line-height: 25px; color: var(--mauve-text); }
  .footer .legal { position: absolute; left: 26px; top: 22px; }
  .follow { position: absolute; right: 28px; top: 22px; display: flex; align-items: center; gap: 14px; font-size: 18px; letter-spacing: 1px; color: #4c4244; }

  .shed-band { position: absolute; left: 0; top: 3086px; width: 1200px; height: 86px;
    background: repeating-linear-gradient(180deg, var(--stripe-dark) 0 7px, var(--stripe-light) 7px 14px); }
</style>
</head>
<body>
  <div class="notice">You're getting this email because you joined us. Not feelin' it?&nbsp;<a href="#">Unsubscribe</a></div>

  <main class="sheet">
    <header class="masthead">
      <div class="brand">BERTOLVI</div>
      <div class="brand-sub">Single Vineyard</div>
      <hr>
      <nav class="nav">
        <span>VINEYARD</span><span class="dot">•</span>
        <span>WINEMAKING</span><span class="dot">•</span>
        <span>WINES</span><span class="dot">•</span>
        <span>HOUSE</span><span class="dot">•</span>
        <span>CONTACT US</span>
      </nav>
    </header>

    <div class="hero" role="img" aria-label="Misty morning at the vineyard: tall gum trees in fog, weathered timber posts, ornamental grasses and the corner of a corrugated iron shed"></div>

    <h1 class="headline">Bertolvi – Italian for ‘shed’</h1>
    <div class="rule upper"></div>
    <div class="facts">
      25 acres in the Southern Highlands, NSW<br>
      architecturally designed house<br>
      three acres under vine: Pinot Gris and Pinot Noir
    </div>
    <div class="rule lower"></div>

    <section class="feature vineyard">
      <div class="photo" role="img" aria-label="Close-up of a bunch of dark Pinot Noir grapes"></div>
      <h2>VINEYARD</h2>
      <p>We chose varieties that would be ideal for the terroir – three clones: Pinot Gris 117, the more traditional Pinot Noir 115 and the newer Pinot Noir 777 – just an acre of each.</p>
      <a class="more" href="#">READ MORE</a>
    </section>

    <section class="feature winemaking">
      <div class="photo" role="img" aria-label="Oak wine barrel head marked in white chalk"></div>
      <h2>WINEMAKING</h2>
      <p>We first met winemaker extraordinaire Tom Ashdale in the Southern Highlands, before our first vintage. wines he's produced.</p>
      <a class="more" href="#">READ MORE</a>
    </section>

    <section class="release">
      <div class="wine" role="img" aria-label="Red wine being poured from a barrel into a glass"></div>
      <div class="release-copy">
        <div class="title">PINOT NOIR<br>2011</div>
        <div class="source">FROM GRAHAM PELL’S 2014<br>AUSTRALIAN CELLAR GUIDE<br>(WWW.CELLARGUIDE.COM.AU):</div>
        <div class="order">
          <svg width="14" height="18" viewBox="0 0 14 18" aria-hidden="true"><polygon points="0,0 14,9 0,18" fill="#1e1e1e"/></svg>
          ORDER NOW
        </div>
      </div>
    </section>

    <div class="rule closing"></div>
    <div class="tasting">
      <p>Light red, early colour development; a fragrant red cherry and strawberry bouquet leads into a lightbodied, but well-balanced, palate with gentle red berry and spice flavours, and just enough depth to satisfy. Drink soon. Rating 90 – to 2015.</p>
      <p class="served">Served in Sydney at Tidewater, Breaker Restaurant, Cafe Lune, Caffe Sorrel,<br>Hattie's Place, Marlin Bay Hotel &amp; Fenno</p>
    </div>
  </main>

  <footer class="footer">
    <div class="legal">© COPYRIGHT BERTOLVI, All rights reserved.<br>25 acres in the Southern Highlands, NSW</div>
    <div class="follow">
      FOLLOW US
      <svg width="48" height="48" viewBox="0 0 48 48" aria-hidden="true"><circle cx="24" cy="24" r="21" fill="none" stroke="#5a4f51" stroke-width="2.5"/></svg>
      <svg width="48" height="48" viewBox="0 0 48 48" aria-hidden="true"><circle cx="24" cy="24" r="21" fill="none" stroke="#5a4f51" stroke-width="2.5"/></svg>
    </div>
  </footer>
  <div class="shed-band"></div>
</body>
</html>
```